Business Card Design

We are a cutting edge natural health care provider who specializes in neuro behavioral conditions. We use brain mapping, neurofeedback, functional neurology and functional medicine to help people achieve their health goals.
We need a business card design for a new office. Would like to position ourselves as an upscale/concierge level treatment center that provides hope and results to people with chronic conditions. We would like the card to feature a brain, possibly a die cut shape. Design needs to communicate our tag line of "providing excellent care for difficult cases."
On back side of card:
By retraining abnormal brainwave patterns and eliminating metabolic problems, our programs often improve symptoms of:
ADD/ADHD
Addiction
Anxiety
Autism
Depression
Fibromyalgia
Insomnia
Memory Loss
Sensory/Motor Dysfunction

Target Market(s)

30-60 year olds with chronic conditions (Anxiety, depression,) or parents of children with chronic conditions (ADHD, autism, learning disorders, etc)

Industry/Entity Type

Health

Contact Information for Business Card

The Halvorsen Clinic
Dr. Colin Halvorsen, DC
4260 Orchard Pkwy. Suite 207
Fernvale, GA 30418
(555) 418-6623
Fax (555) 418-7044
www.TheHalvorsenClinic.example
www.DrColinHalvorsen.example

Requirements
Nice to have
• Picture of a brain that really pops on the page.

```html
<!DOCTYPE html>
<html lang="en">
<head>
<meta charset="UTF-8">
<title>The Halvorsen Clinic — Business Card</title>
<link rel="stylesheet" href="https://fonts.googleapis.com/css2?family=Source+Sans+3:wght@400;600;700&display=swap">
<style>
  :root {
    --card-bg: #ffffff;
    --page-bg: #ffffff;
    --ink: #1e1e1e;
    --ink-soft: #2a2a2a;
    --brand-green: #22b04b;
    --card-edge: #8a8a8a;
  }
  html, body {
    margin: 0;
    padding: 0;
    width: 1200px;
    height: 700px;
    overflow: hidden;
    background: var(--page-bg);
  }
  .business-card {
    position: relative;
    width: 1200px;
    height: 700px;
    box-sizing: border-box;
    background: var(--card-bg);
    border: 2px solid var(--card-edge);
    font-family: "Source Sans 3", "Myriad Pro", Arial, sans-serif;
    color: var(--ink);
  }
  .brand-mark {
    position: absolute;
    left: 160px;
    top: 70px;
    width: 220px;
    height: 220px;
  }
  .clinic-name {
    position: absolute;
    left: 96px;
    top: 440px;
    margin: 0;
    font-size: 50px;
    font-weight: 400;
    letter-spacing: 0.2px;
    color: var(--ink);
    white-space: nowrap;
  }
  .doctor-name {
    position: absolute;
    left: 672px;
    top: 88px;
    margin: 0;
    font-size: 44px;
    font-weight: 700;
    color: var(--ink);
    white-space: nowrap;
  }
  .contact-block {
    position: absolute;
    left: 746px;
    top: 246px;
    height: 194px;
    border-left: 4px solid var(--brand-green);
    box-sizing: border-box;
  }
  .contact-list {
    list-style: none;
    margin: 0;
    padding: 0;
    font-size: 20px;
    color: var(--ink-soft);
  }
  .contact-list li {
    position: absolute;
    left: 22px;
    white-space: nowrap;
  }
  .contact-phone-main { top: 20px; }
  .contact-phone-fax  { top: 64px; }
  .contact-list .contact-web-clinic { top: 113px; left: 28px; }
  .contact-list .contact-web-doctor { top: 159px; left: 28px; }
  .office-address {
    position: absolute;
    left: 674px;
    top: 492px;
    margin: 0;
    font-size: 20px;
    color: var(--ink-soft);
    white-space: nowrap;
    font-style: normal;
  }
</style>
</head>
<body>
  <main class="business-card">
    <svg class="brand-mark" viewBox="0 0 220 220" aria-hidden="true">
      <circle cx="110" cy="110" r="110" fill="var(--brand-green)"/>
    </svg>
    <h1 class="clinic-name">The Halvorsen Clinic</h1>

    <h2 class="doctor-name">Dr. Colin Halvorsen</h2>

    <div class="contact-block">
      <ul class="contact-list">
        <li class="contact-phone-main">(555) 418-6623</li>
        <li class="contact-phone-fax">(555) 418-7044</li>
        <li class="contact-web-clinic">www.TheHalvorsenClinic.example</li>
        <li class="contact-web-doctor">www.DrColinHalvorsen.example</li>
      </ul>
    </div>

    <address class="office-address">DC 4260 Orchard Pkwy. Suite 207 Fernvale, GA 30418</address>
  </main>
</body>
</html>
```